Plumber needs a business card

I need a new business card for my plumbing business. I dont have a logo at the moment but I want business cards that are simple but very professional. I want to look like
Name: Milo Brenton
Address: (just make one up)
Phone: 0497 318 264
Email: milo@fernpost.net
Colors to use:
Blacks, blues, silvers

```html
<!DOCTYPE html>
<html lang="en">
<head>
<meta charset="utf-8">
<title>Milo Brenton – Business Card</title>
<link rel="stylesheet" href="https://fonts.googleapis.com/css2?family=Cinzel:wght@500;600&family=Questrial&display=swap">
<style>
  :root {
    --stage: #000000;
    --card-white: #ffffff;
    --blue-deep: #0a5a86;
    --blue-mid: #0f74a8;
    --blue-bright: #00b6e8;
    --silver: #c9d1da;
    --navy-edge: #1b1f4a;
    --contact-blue: #1a7db0;
    --icon-blue: #137fb5;
  }
  html, body {
    margin: 0;
    padding: 0;
    width: 1200px;
    height: 1020px;
    overflow: hidden;
    background: var(--stage);
  }
  .card {
    position: absolute;
    left: 100px;
    top: 223px;
    width: 1000px;
    height: 573px;
    background: var(--card-white);
    overflow: hidden;
  }
  .card-art {
    position: absolute;
    inset: 0;
    width: 1000px;
    height: 573px;
  }
  .identity {
    position: absolute;
    left: 112px;
    top: 240px;
    color: var(--card-white);
  }
  .identity-name {
    margin: 0;
    font-family: "Cinzel", serif;
    font-weight: 500;
    font-size: 36px;
    line-height: 1;
    letter-spacing: 0.3px;
  }
  .identity-role {
    margin: 6px 0 0 0;
    font-family: "Cinzel", serif;
    font-weight: 500;
    font-size: 23px;
    line-height: 1;
    letter-spacing: 7.4px;
  }
  .contact-item {
    position: absolute;
    left: 573px;
    display: flex;
    align-items: flex-start;
    gap: 21px;
  }
  .contact-item--address { top: 185px; }
  .contact-item--reach { top: 324px; }
  .contact-icon {
    width: 40px;
    height: 40px;
    flex: none;
    margin-top: 2px;
  }
  .contact-text {
    margin: 0;
    font-family: "Questrial", sans-serif;
    font-size: 28px;
    line-height: 28px;
    color: var(--contact-blue);
  }
</style>
</head>
<body>
  <div class="card">
    <svg class="card-art" viewBox="0 0 1000 573">
      <defs>
        <radialGradient id="panelGlow" cx="490" cy="300" r="470" gradientUnits="userSpaceOnUse">
          <stop offset="0" stop-color="var(--blue-bright)"/>
          <stop offset="0.35" stop-color="var(--blue-mid)"/>
          <stop offset="1" stop-color="var(--blue-deep)"/>
        </radialGradient>
        <linearGradient id="arcEdge" x1="0" y1="0" x2="0" y2="1">
          <stop offset="0" stop-color="var(--navy-edge)"/>
          <stop offset="0.5" stop-color="var(--silver)"/>
          <stop offset="1" stop-color="var(--navy-edge)"/>
        </linearGradient>
      </defs>
      <path class="blue-panel" role="img" aria-label="Blue panel with a subtle interlocking pipe pattern"
            d="M0 0 H327 A325 325 0 0 1 327 573 H0 Z" fill="url(#panelGlow)"/>
      <path class="panel-edge" d="M327 0 A325 325 0 0 1 327 573"
            fill="none" stroke="url(#arcEdge)" stroke-width="4"/>
    </svg>

    <div class="identity">
      <p class="identity-name">Milo Brenton</p>
      <p class="identity-role">Designation</p>
    </div>

    <div class="contact-item contact-item--address">
      <svg class="contact-icon" viewBox="0 0 40 40" aria-hidden="true">
        <circle cx="20" cy="20" r="20" fill="var(--icon-blue)"/>
        <path d="M20 10 L30 19 H27 V28 H22.5 V22 H17.5 V28 H13 V19 H10 Z" fill="#fff"/>
      </svg>
      <p class="contact-text">18/64<br>Harbour Lane<br>Brookvale - 2100<br>Australia</p>
    </div>

    <div class="contact-item contact-item--reach">
      <svg class="contact-icon" viewBox="0 0 40 40" aria-hidden="true">
        <circle cx="20" cy="20" r="20" fill="var(--icon-blue)"/>
        <path d="M14 10 C12 11 11 13 12 16 C14 22 18 27 24 30 C27 31 29 30 30 28 L26.5 24.5 L23.5 26 C20.5 24 17.5 21 16 18 L17.5 15 Z" fill="#fff"/>
      </svg>
      <p class="contact-text">Phone: 0497 318 264<br>Email: milo@fernpost.net</p>
    </div>
  </div>
</body>
</html>
```